Qvo Brightforge Website

All the descriptions are available in the attached file. The designer has to structure the website and find the right images and icons. The website should look modern and avoid using images of real humans rather use animated images. Please note that the design should include home page, all the 4 services page , the contact us would be at the bottom of home page.

```html
<!DOCTYPE html>
<html lang="en">
<head>
<meta charset="utf-8">
<title>Qvo Brightforge – IT Consulting</title>
<link href="https://fonts.googleapis.com/css2?family=Poppins:wght@300;400;500;600;700&display=swap" rel="stylesheet">
<style>
:root{
  --blue:#3272c0;
  --blue-dark:#2863ad;
  --ink:#222;
  --muted:#777;
  --line:#e6e9ef;
  --soft:#f2f3f5;
  --field:#eeeeee;
  --white:#fff;
}
*{margin:0;padding:0;box-sizing:border-box}
html,body{width:1200px;height:3711px;overflow:hidden}
body{font-family:'Poppins',sans-serif;color:var(--ink);background:var(--white);position:relative}
.abs{position:absolute}
a{text-decoration:none;color:inherit}

.topbar{left:0;top:0;width:1200px;height:43px;background:var(--blue);color:#fff;font-size:15px}
.topbar .contacts{right:85px;top:0;height:43px;display:flex;align-items:center;gap:24px;white-space:nowrap}
.topbar .item{display:flex;align-items:center;gap:10px}
.header{left:0;top:43px;width:1200px;height:118px;background:#fff}
.brand{font-weight:600;font-size:26px;color:var(--blue);display:flex;align-items:center;gap:12px;white-space:nowrap}
.brand .dot{width:18px;height:18px;background:var(--blue);border-radius:50%}
.nav{right:85px;top:44px;display:flex;gap:37px;font-size:15px;color:#333}
.nav .active{color:var(--blue);border-bottom:2px solid var(--blue);padding-bottom:9px}

.hero{left:0;top:161px;width:1200px;height:692px;background:linear-gradient(135deg,#3a4250,#2b313c 45%,#5b6068);overflow:hidden}
.hero-title{left:0;width:1200px;top:172px;text-align:center;color:#fff;font-weight:700;font-size:43px;line-height:51px}
.hero-sub{left:0;width:1200px;top:304px;text-align:center;color:#fff;font-size:16px;line-height:26px}
.btn-hero{left:501px;top:398px;width:198px;height:72px;background:var(--blue);color:#fff;font-size:20px;font-weight:500;display:flex;align-items:center;justify-content:center}
.hero svg{position:absolute;left:0;bottom:0}

.section-title{left:0;width:1200px;text-align:center;color:var(--blue);font-weight:700;font-size:30px}
.card{top:974px;width:251px;height:439px;border:1px solid var(--line);box-shadow:0 0 6px rgba(0,0,0,.05);text-align:center}
.card .icon{position:absolute;left:71px;top:24px;width:108px;height:108px;border-radius:50%;background:var(--blue);display:flex;align-items:center;justify-content:center}
.card h3{position:absolute;top:148px;left:0;width:100%;color:var(--blue);font-weight:400;font-size:20px;line-height:26px}
.card p{position:absolute;top:214px;left:18px;right:18px;color:var(--muted);font-size:15px;line-height:26px}
.card .more{position:absolute;top:386px;left:0;width:100%;color:var(--blue);font-size:13px}

.about{left:0;top:1485px;width:1200px;height:587px;background:var(--blue);color:#fff}
.about .photo{left:88px;top:100px;width:436px;height:387px;border-radius:12px;background:linear-gradient(135deg,#6b5a48,#2f2a26 60%,#4a4038)}
.about h2{left:602px;top:96px;font-size:30px;font-weight:700}
.about p{left:602px;top:157px;width:520px;font-size:15.5px;line-height:31px}
.btn-light{left:601px;top:440px;width:157px;height:47px;background:#fff;color:var(--blue);font-size:15px;display:flex;align-items:center;justify-content:center}

.blog{left:0;top:2072px;width:1200px;height:821px;background:var(--soft)}
.post{top:205px;width:327px;height:506px;background:#fff}
.post .img{position:absolute;left:0;top:0;width:327px;height:261px}
.post .date{position:absolute;left:29px;top:37px;width:148px;height:39px;background:#fff;font-size:11px;display:flex;align-items:center;justify-content:center;gap:7px}
.post h3{position:absolute;left:31px;top:283px;width:260px;color:var(--blue);font-weight:400;font-size:22px;line-height:32px}
.post p{position:absolute;left:31px;top:357px;width:270px;color:var(--muted);font-size:14px;line-height:26px}
.post .more{position:absolute;left:31px;top:447px;color:var(--blue);font-size:13px}

.field{background:var(--field);color:#777;font-size:15px;padding:0 20px;display:flex;align-items:center}
.btn-submit{left:315px;top:3354px;width:114px;height:50px;background:var(--blue);color:#fff;font-size:15px;display:flex;align-items:center;justify-content:center}
.info{left:717px;font-size:16px;color:#333;display:flex;align-items:flex-start;gap:16px;white-space:nowrap}
.social{top:3251px;width:44px;height:44px;border:2px solid var(--blue);border-radius:50%}

.footer{left:0;top:3420px;width:1200px;height:291px}
.footer .rule{top:196px;height:1px;background:rgba(255,255,255,.35)}
.footer .copy{left:87px;top:228px;color:#fff;font-size:14px}
.footer .links{right:85px;top:228px;color:#fff;font-size:14px;display:flex;gap:12px}
</style>
</head>
<body>

<div class="abs topbar">
  <div class="abs contacts">
    <div class="item">
      <svg width="28" height="20" viewBox="0 0 28 20"><rect x="1" y="1" width="26" height="18" fill="none" stroke="#fff" stroke-width="2"/><path d="M1 1 L14 11 L27 1" fill="none" stroke="#fff" stroke-width="2"/></svg>
      hello@qvobrightforge.example
    </div>
    <div class="item">
      <svg width="22" height="22" viewBox="0 0 24 24"><path d="M6.6 10.8a15 15 0 0 0 6.6 6.6l2.2-2.2c.3-.3.7-.4 1-.2 1.1.4 2.3.6 3.6.6.6 0 1 .4 1 1V20c0 .6-.4 1-1 1A17 17 0 0 1 3 4c0-.6.4-1 1-1h3.5c.6 0 1 .4 1 1 0 1.3.2 2.5.6 3.6.1.3 0 .7-.2 1z" fill="#fff"/></svg>
      +61 (08) 5550 0142
    </div>
  </div>
</div>

<header class="abs header">
  <div class="abs brand" style="left:87px;top:38px"><span class="dot"></span>Qvo Brightforge</div>
  <nav class="abs nav">
    <a class="active">Home</a><a>Services</a><a>Products</a><a>Blog</a><a>Contact Us</a>
  </nav>
</header>

<section class="abs hero" role="img" aria-label="Overhead view of a team working on laptops at a shared desk">
  <h1 class="abs hero-title">ADVANCING INNOVATION<br>THROUGH IT CONSULTING</h1>
  <p class="abs hero-sub">Empower your digital journey with our advanced IT solutions. From<br>data to web and mobile apps, we've got you covered.</p>
  <a class="abs btn-hero">Know More</a>
  <svg width="1200" height="110" viewBox="0 0 1200 110">
    <path d="M0 110 L0 95 Q600 -40 1200 95 L1200 110 Z" fill="var(--blue)"/>
    <path d="M0 110 Q600 -10 1200 110 Z" fill="#fff"/>
  </svg>
</section>

<h2 class="abs section-title" style="top:873px">OUR SERVICES</h2>

<div class="abs card" style="left:86px">
  <div class="icon"><svg width="40" height="46" viewBox="0 0 40 46"><path d="M4 2h22l10 10v32H4z" fill="#fff"/><rect x="10" y="22" width="20" height="2.5" fill="var(--blue)"/><rect x="10" y="28" width="20" height="2.5" fill="var(--blue)"/><rect x="10" y="34" width="20" height="2.5" fill="var(--blue)"/><rect x="22" y="10" width="3" height="8" fill="var(--blue)"/><rect x="27" y="13" width="3" height="5" fill="var(--blue)"/></svg></div>
  <h3>DATA<br>ANALYTICS</h3>
  <p>At Qvo Brightforge, our proficiency consists of linking your leadership team's objectives with the relevant data that holds significance.</p>
  <a class="more">READ MORE</a>
</div>
<div class="abs card" style="left:346px">
  <div class="icon"><svg width="54" height="44" viewBox="0 0 54 44"><rect x="20" y="4" width="30" height="22" rx="2" fill="none" stroke="#fff" stroke-width="3"/><circle cx="11" cy="12" r="6" fill="#fff"/><path d="M2 40 Q4 22 11 22 Q18 22 20 32 L36 32 L36 36 L2 40Z" fill="#fff"/><rect x="14" y="34" width="36" height="4" fill="#fff"/></svg></div>
  <h3>WEB<br>DEVELOPMENT</h3>
  <p>At Qvo Brightforge, we are a trailblazing web development company committed to delivering cutting-edge digital solutions</p>
  <a class="more">READ MORE</a>
</div>
<div class="abs card" style="left:605px">
  <div class="icon"><svg width="28" height="48" viewBox="0 0 28 48"><rect x="2" y="2" width="24" height="44" rx="4" fill="#fff"/><rect x="5" y="8" width="18" height="30" fill="var(--blue)"/><circle cx="14" cy="42" r="2" fill="var(--blue)"/></svg></div>
  <h3>MOBILE APP<br>DEVELOPMENT</h3>
  <p>At Qvo Brightforge, we are a pioneering mobile app development company dedicated to crafting exceptional digital experiences</p>
  <a class="more">READ MORE</a>
</div>
<div class="abs card" style="left:864px">
  <div class="icon"><svg width="54" height="40" viewBox="0 0 54 40"><circle cx="27" cy="10" r="7" fill="#fff"/><circle cx="12" cy="14" r="5" fill="#fff"/><circle cx="42" cy="14" r="5" fill="#fff"/><path d="M15 36 Q15 20 27 20 Q39 20 39 36Z" fill="#fff"/><path d="M2 34 Q2 22 12 22 Q16 22 17 24 Q13 28 13 34Z" fill="#fff"/><path d="M52 34 Q52 22 42 22 Q38 22 37 24 Q41 28 41 34Z" fill="#fff"/></svg></div>
  <h3>START-UP<br>TECH PARTNER</h3>
  <p>At Qvo Brightforge, we are committed to supporting early-stage start-ups on their journey to success by providing comprehensive technical partner services.</p>
  <a class="more">READ MORE</a>
</div>

<section class="abs about">
  <div class="abs photo" role="img" aria-label="Illustration of a consultant working at a laptop in an office"></div>
  <h2 class="abs">ABOUT QVO BRIGHTFORGE</h2>
  <p class="abs">We are a forward-thinking IT consulting firm specializing in providing cutting-edge data analytics, web application development, and mobile app development services. Our passion for innovation and technology drives us to deliver tailor-made solutions that empower businesses to thrive in the digital landscape. We take pride in our ability to collaborate with early-stage startups as their technology partner, helping them navigate the challenges of launching and scaling their ventures.</p>
  <a class="abs btn-light">Read More</a>
</section>

<section class="abs blog">
  <h2 class="abs section-title" style="top:105px">OUR LATEST BLOG</h2>
  <article class="abs post" style="left:86px">
    <div class="img" role="img" aria-label="Illustration of two colleagues reviewing notes at a laptop" style="background:linear-gradient(135deg,#c9b8a6,#8b7766)"></div>
    <div class="date"><svg width="12" height="12" viewBox="0 0 12 12"><rect x="1" y="2" width="10" height="9" fill="none" stroke="var(--blue)" stroke-width="1.5"/><rect x="1" y="2" width="10" height="3" fill="var(--blue)"/></svg>MAY 12, 2023</div>
    <h3>Lorem ipsum dolor sit consectetur</h3>
    <p>Pellentesque vitae nulla nec dui dapibus aliquet et ac massa. Class aptent taciti sociosqu ad litora</p>
    <a class="more">Know More</a>
  </article>
  <article class="abs post" style="left:438px">
    <div class="img" role="img" aria-label="Illustration of a meeting at a desk with a scale of justice" style="background:linear-gradient(135deg,#d8dce2,#6f7682)"></div>
    <div class="date"><svg width="12" height="12" viewBox="0 0 12 12"><rect x="1" y="2" width="10" height="9" fill="none" stroke="var(--blue)" stroke-width="1.5"/><rect x="1" y="2" width="10" height="3" fill="var(--blue)"/></svg>MAY 12, 2023</div>
    <h3>Lorem ipsum dolor sit consectetur</h3>
    <p>Pellentesque vitae nulla nec dui dapibus aliquet et ac massa. Class aptent taciti sociosqu ad litora</p>
    <a class="more">Know More</a>
  </article>
  <article class="abs post" style="left:788px">
    <div class="img" role="img" aria-label="Illustration of a team reading documents in a library office" style="background:linear-gradient(135deg,#8a7d70,#d7cfc4)"></div>
    <div class="date"><svg width="12" height="12" viewBox="0 0 12 12"><rect x="1" y="2" width="10" height="9" fill="none" stroke="var(--blue)" stroke-width="1.5"/><rect x="1" y="2" width="10" height="3" fill="var(--blue)"/></svg>MAY 12, 2023</div>
    <h3>Lorem ipsum dolor sit consectetur</h3>
    <p>Pellentesque vitae nulla nec dui dapibus aliquet et ac massa. Class aptent taciti sociosqu ad litora</p>
    <a class="more">Know More</a>
  </article>
</section>

<h2 class="abs section-title" style="top:2978px">CONTACT US</h2>
<div class="abs field" style="left:148px;top:3063px;width:218px;height:46px">First Name*</div>
<div class="abs field" style="left:380px;top:3063px;width:218px;height:46px">Last Name*</div>
<div class="abs field" style="left:148px;top:3123px;width:218px;height:46px">Phone*</div>
<div class="abs field" style="left:380px;top:3123px;width:218px;height:46px">Email*</div>
<div class="abs field" style="left:148px;top:3184px;width:450px;height:148px;align-items:flex-start;padding-top:14px">Message*</div>
<a class="abs btn-submit">SUBMIT</a>

<div class="abs info" style="top:3092px;line-height:26px;font-size:15px">
  <svg width="18" height="24" viewBox="0 0 18 24" style="margin-top:2px"><path d="M9 1a8 8 0 0 0-8 8c0 6 8 14 8 14s8-8 8-14a8 8 0 0 0-8-8z" fill="var(--blue)"/><circle cx="9" cy="9" r="3" fill="#fff"/></svg>
  <span>Suite 12/40 Harbour Lane,<br>Eastvale WA 6100</span>
</div>
<div class="abs info" style="top:3148px;font-size:21px;align-items:center">
  <svg width="22" height="22" viewBox="0 0 24 24"><path d="M6.6 10.8a15 15 0 0 0 6.6 6.6l2.2-2.2c.3-.3.7-.4 1-.2 1.1.4 2.3.6 3.6.6.6 0 1 .4 1 1V20c0 .6-.4 1-1 1A17 17 0 0 1 3 4c0-.6.4-1 1-1h3.5c.6 0 1 .4 1 1 0 1.3.2 2.5.6 3.6.1.3 0 .7-.2 1z" fill="var(--blue)"/></svg>
  +61 (08) 5550 0142
</div>
<div class="abs info" style="top:3196px;align-items:center">
  <svg width="24" height="17" viewBox="0 0 28 20"><rect x="1" y="1" width="26" height="18" fill="var(--blue)"/><path d="M1 1 L14 11 L27 1" fill="none" stroke="#fff" stroke-width="2"/></svg>
  hello@qvobrightforge.example
</div>
<div class="abs social" style="left:718px"></div>
<div class="abs social" style="left:769px"></div>
<div class="abs social" style="left:819px"></div>
<div class="abs social" style="left:870px"></div>

<footer class="abs footer">
  <svg class="abs" style="left:0;top:0" width="1200" height="291" viewBox="0 0 1200 291">
    <path d="M0 8 Q600 110 1200 8 L1200 291 L0 291Z" fill="#6f7379"/>
    <path d="M0 16 Q600 130 1200 16 L1200 291 L0 291Z" fill="var(--blue-dark)"/>
    <path d="M0 26 Q600 140 1200 26 L1200 291 L0 291Z" fill="var(--blue)"/>
  </svg>
  <div class="abs rule" style="left:87px;width:380px"></div>
  <div class="abs rule" style="left:733px;width:380px"></div>
  <div class="abs brand" style="left:0;width:1200px;top:176px;justify-content:center;color:#fff"><span class="dot" style="background:#fff"></span>Qvo Brightforge</div>
  <div class="abs copy">Copyright © 2023 All Rights Reserved By QVO BRIGHTFORGE</div>
  <div class="abs links"><a>Services</a><span>|</span><a>Products</a><span>|</span><a>Blog</a><span>|</span><a>Contact Us</a></div>
</footer>

</body>
</html>
```